Atelier Marrow Architecture business card

We need to update our business card. We do high end custom residential, hospitality, and wellness architecture. We focus on creating unique spaces and design around the five senses, believing that architecture's true impact is not on our surroundings, but within us. We would like to see designs are instill a sense of calm awe. They should be crisp, fresh, clean, authentic, & contemporary without being sterile, overworked, or harsh. White space is important. Alternative materials are an option if natural. We have created our own logo and would like designs to incorporate it. However, we are willing to see alternatives if the logo becomes a stumbling block and you have an alternate you suggest. Card must have the following information:
Atelier Marrow Architecture, Inc.
728 Holloway Ct. NE Atlanta, GA 30318
Marcus T. Whitcombe, AIA, NCARB, LEED AP BD+C
ateliermarrow.example

Target Market(s)

Higher net worth individuals with an appreciation for design, nature, sustainability,

Industry/Entity Type

Architect

Contact Information for Business Card

See above. The title of Owner or Architect is helpful but not necessary. Minimalism should trump additional information.

Font styles to use
Serif
Sans Serif

Requirements
Must have
• It should look professional. It must use logo
Should not have
• caligraphy, animals, anything that is cute,

```html
<!DOCTYPE html>
<html lang="en">
<head>
<meta charset="utf-8">
<title>Atelier Marrow Architecture — Business Card</title>
<link href="https://fonts.googleapis.com/css2?family=Lato:ital,wght@0,400;0,700;1,300&family=Marcellus&display=swap" rel="stylesheet">
<style>
  :root {
    --page: #efeeec;
    --card-white: #ffffff;
    --panel-grey: #e6e6e8;
    --ink: #2a2a2a;
    --ink-soft: #3c3c3c;
    --rule-teal: #1f5a63;
    --icon-dark: #1e1e1e;
    --band-dark: #262626;
    --band-mid: #3e3e3e;
  }
  * { box-sizing: border-box; margin: 0; padding: 0; }
  html, body { width: 1200px; height: 900px; overflow: hidden; }
  body {
    background: var(--page);
    display: flex;
    flex-direction: column;
    align-items: center;
    justify-content: center;
    gap: 56px;
    font-family: "Lato", Arial, sans-serif;
  }
  .card {
    width: 640px;
    height: 366px;
    background: var(--card-white);
    position: relative;
    display: flex;
    box-shadow: 0 6px 18px rgba(0,0,0,0.12);
  }
  .edge-band {
    width: 38px;
    height: 100%;
    flex: none;
    background: linear-gradient(180deg, var(--band-dark) 0%, var(--band-mid) 50%, var(--band-dark) 100%);
  }

  /* front */
  .front-face {
    flex: 1;
    display: flex;
    align-items: center;
    justify-content: center;
  }
  .wordmark {
    font-family: "Marcellus", Georgia, serif;
    color: var(--ink-soft);
    font-size: 30px;
    letter-spacing: 0.14em;
    text-transform: uppercase;
    text-align: center;
    line-height: 1.3;
  }

  /* back */
  .contact-panel {
    width: 372px;
    background: var(--panel-grey);
    padding-top: 52px;
  }
  .contact-row {
    display: flex;
    align-items: center;
    gap: 14px;
    padding: 0 0 0 34px;
    border-bottom: 1.5px solid var(--rule-teal);
  }
  .contact-row.name-row { padding-bottom: 10px; }
  .contact-row.web-row { padding: 10px 0 10px 34px; }
  .contact-row.address-row { border-bottom: none; padding-top: 18px; align-items: flex-start; }
  .icon {
    width: 30px; height: 30px;
    border-radius: 50%;
    background: var(--icon-dark);
    flex: none;
    display: flex; align-items: center; justify-content: center;
  }
  .icon.small { width: 24px; height: 24px; }
  .person-name {
    font-weight: 700;
    font-size: 18px;
    color: var(--ink);
    text-transform: uppercase;
    letter-spacing: 0.02em;
  }
  .credentials {
    font-weight: 300;
    font-style: italic;
    font-size: 15px;
    color: var(--ink);
  }
  .web-address { font-size: 12px; color: var(--ink); }
  .street-address { font-size: 15px; color: var(--ink); line-height: 1.3; margin-top: 4px; }
  .address-row .icon { margin-top: 14px; }
  .logo-panel {
    flex: 1;
    padding: 28px 0 0 22px;
  }
  .logo-panel .wordmark {
    font-size: 15px;
    text-align: left;
    letter-spacing: 0.12em;
  }
</style>
</head>
<body>

  <section class="card card-front" aria-label="Card front">
    <div class="edge-band" role="img" aria-label="Dark grey decorative edge band"></div>
    <div class="front-face">
      <p class="wordmark">Atelier Marrow<br>Architecture</p>
    </div>
    <div class="edge-band" role="img" aria-label="Dark grey decorative edge band"></div>
  </section>

  <section class="card card-back" aria-label="Card back">
    <div class="contact-panel">
      <div class="contact-row name-row">
        <span class="icon">
          <svg width="18" height="18" viewBox="0 0 18 18" aria-hidden="true">
            <circle cx="9" cy="6" r="3.6" fill="#fff"/>
            <path d="M2.5 17 C2.5 11.5 15.5 11.5 15.5 17 Z" fill="#fff"/>
          </svg>
        </span>
        <div>
          <p class="person-name">Marcus T. Whitcombe</p>
          <p class="credentials">AIA, NCARB, LEED AP BD+C</p>
        </div>
      </div>
      <div class="contact-row web-row">
        <span class="icon small">
          <svg width="16" height="16" viewBox="0 0 16 16" aria-hidden="true" fill="none" stroke="#fff" stroke-width="1.2">
            <circle cx="8" cy="8" r="6.5"/>
            <ellipse cx="8" cy="8" rx="3" ry="6.5"/>
            <line x1="1.5" y1="8" x2="14.5" y2="8"/>
            <line x1="2.5" y1="4.8" x2="13.5" y2="4.8"/>
            <line x1="2.5" y1="11.2" x2="13.5" y2="11.2"/>
          </svg>
        </span>
        <p class="web-address">ateliermarrow.example</p>
      </div>
      <div class="contact-row address-row">
        <span class="icon small">
          <svg width="14" height="14" viewBox="0 0 14 14" aria-hidden="true">
            <path d="M7 1.5 L13 7 H11 V12.5 H8.3 V9 H5.7 V12.5 H3 V7 H1 Z" fill="#fff"/>
          </svg>
        </span>
        <p class="street-address">728 Holloway Ct. NE Atlanta,<br>GA 30318</p>
      </div>
    </div>
    <div class="logo-panel">
      <p class="wordmark">Atelier Marrow<br>Architecture</p>
    </div>
    <div class="edge-band" role="img" aria-label="Dark grey decorative edge band"></div>
  </section>

</body>
</html>
```